11x 11 - KIVO Program Flyer

Introducing The KIVO PROGRAM

The BEST DPA Product on the Planet
* Lowest Zarn in the Industry - 580 Minimum
* Nothing Down - 100% GTU Purchase Financing
* One Submission, One Approval and One Closing
* No Income Limits, No DTI Restrictions, No Property Restrictions

Call (800) 471-9026 for more information

RLCB #738160
www.2ndlanehomes.com

```html
<!DOCTYPE html>
<html lang="en">
<head>
<meta charset="utf-8">
<title>KIVO Program Flyer</title>
<link rel="stylesheet" href="https://fonts.googleapis.com/css2?family=Montserrat:wght@600;700;800&family=Roboto+Condensed:wght@400&display=swap">
<style>
  :root {
    --sky-top: #bcd7ef;
    --sky-mid: #e4eef8;
    --paper: #f4f7fb;
    --tab-blue: #6fa6d8;
    --brand-red: #c8202f;
    --ink: #111418;
    --deep-blue: #0c5e8a;
    --call-blue: #175c8a;
    --navy: #0f2b4d;
    --check-green: #7cc242;
    --strip-gray: #b9b6b7;
    --logo-gold: #b89b3c;
  }
  * { margin: 0; padding: 0; box-sizing: border-box; }
  html, body { width: 1200px; height: 1200px; overflow: hidden; background: #fff; }
  .flyer {
    position: relative; width: 1200px; height: 1200px; overflow: hidden;
    background: linear-gradient(180deg, var(--sky-top) 0%, var(--sky-mid) 45%, var(--paper) 100%);
    font-family: "Roboto Condensed", "Arial Narrow", sans-serif;
  }
  .fabric-wave { position: absolute; left: 0; top: 70px; width: 1200px; height: 620px; }
  .photo-couple {
    position: absolute; left: 0; top: 378px; width: 508px; height: 660px;
    background: linear-gradient(180deg, #e9e4de 0%, #c7a98f 60%, #b58a6c 85%, #c9b6a8 100%);
  }
  .intro-tab {
    position: absolute; left: 614px; top: 0; width: 291px; height: 106px;
    background: var(--tab-blue); border-radius: 0 0 6px 6px;
    color: #fff; font-family: "Montserrat", sans-serif; font-weight: 600;
    font-size: 24px; letter-spacing: 6px; text-align: center; line-height: 136px;
  }
  .headline { position: absolute; left: 606px; top: 128px; height: 120px; width: 540px; }
  .headline-the {
    position: absolute; left: 0; top: 28px; transform-origin: left top;
    transform: rotate(-90deg) translate(-84px, 0);
    font-family: "Montserrat", sans-serif; font-weight: 600; font-size: 54px;
    color: var(--brand-red); line-height: 60px;
  }
  .headline-name {
    position: absolute; left: 76px; top: -2px;
    font-family: "Montserrat", sans-serif; font-weight: 800; font-size: 136px;
    line-height: 120px; color: var(--brand-red); letter-spacing: -1px;
  }
  .tagline {
    position: absolute; left: 617px; top: 248px;
    font-family: "Montserrat", sans-serif; font-weight: 700; font-size: 29px; color: var(--ink);
  }
  .company-mark {
    position: absolute; left: 822px; top: 392px; display: flex; align-items: center; gap: 10px;
    font-family: "Montserrat", sans-serif; font-weight: 700; font-size: 19px; color: var(--deep-blue);
  }
  .company-mark .mark-dot { width: 20px; height: 20px; border-radius: 50%; background: var(--logo-gold); }
  .benefits { position: absolute; left: 614px; top: 697px; color: var(--ink); }
  .benefits h2 { font-weight: 400; font-size: 33px; margin-bottom: 10px; }
  .benefits ul { list-style: none; }
  .benefits li { display: flex; align-items: flex-start; font-size: 25px; line-height: 32px; margin-bottom: 6px; }
  .benefits li svg { flex: none; width: 28px; height: 28px; margin: 2px 16px 0 14px; }
  .call-to-action {
    position: absolute; left: 614px; top: 966px; width: 505px; text-align: center;
    font-family: "Montserrat", sans-serif; font-weight: 700; color: var(--call-blue);
  }
  .call-number { font-size: 45px; line-height: 52px; text-align: left; letter-spacing: 1.5px; white-space: nowrap; }
  .call-sub { font-size: 34px; line-height: 44px; text-align: left; letter-spacing: 1px; white-space: nowrap; }
  .call-web { font-family: "Roboto Condensed", sans-serif; font-weight: 400; font-size: 26px; line-height: 32px; color: var(--ink); margin-top: 4px; }
  .footer-band { position: absolute; left: 0; top: 1027px; width: 1200px; height: 121px; }
  .footer-strip { position: absolute; left: 0; top: 1148px; width: 508px; height: 52px; background: var(--strip-gray); }
  .housing-badge { position: absolute; left: 68px; top: 1045px; width: 90px; height: 86px; background: #fff; border-radius: 4px; }
  .footer-divider { position: absolute; left: 184px; top: 1040px; width: 1px; height: 92px; background: rgba(255,255,255,.6); }
  .license { position: absolute; left: 222px; top: 1073px; color: #fff; font-size: 25px; line-height: 32px; }
</style>
</head>
<body>
<main class="flyer">
  <svg class="fabric-wave" viewBox="0 0 1200 620" role="img" aria-label="Flowing navy silk fabric banner sweeping across the sky">
    <defs>
      <linearGradient id="silk" x1="0" y1="0" x2="1" y2="1">
        <stop offset="0" stop-color="#4f7fae"/>
        <stop offset="0.35" stop-color="#2d5888"/>
        <stop offset="0.7" stop-color="#132f55"/>
        <stop offset="1" stop-color="#1e4a7a"/>
      </linearGradient>
    </defs>
    <path d="M0 5 C120 -5 300 10 420 130 C520 230 560 290 700 290 C820 290 880 400 1000 450 C1100 490 1170 470 1200 440 L1200 560 C1120 610 960 600 860 520 C780 460 720 400 620 390 C520 380 420 360 330 320 C220 270 100 260 0 300 Z" fill="url(#silk)" opacity="0.92"/>
  </svg>

  <div class="photo-couple" role="img" aria-label="Happy couple unpacking moving boxes in their new home"></div>

  <div class="intro-tab">INTRODUCING</div>

  <h1 class="headline">
    <span class="headline-the">the</span>
    <span class="headline-name">KIVO</span>
  </h1>
  <p class="tagline">When “nothing” is all you need</p>

  <div class="company-mark"><span class="mark-dot"></span>Second Lane Home Lending, Inc.</div>

  <section class="benefits">
    <h2>The BEST DPA Product on the Planet</h2>
    <ul>
      <li><svg viewBox="0 0 28 28"><circle cx="14" cy="14" r="13" fill="var(--check-green)"/><path d="M8 14.5l4 4 8-9" fill="none" stroke="#fff" stroke-width="3" stroke-linecap="round" stroke-linejoin="round"/></svg>Lowest Zarn in the Industry - 580 Minimum</li>
      <li><svg viewBox="0 0 28 28"><circle cx="14" cy="14" r="13" fill="var(--check-green)"/><path d="M8 14.5l4 4 8-9" fill="none" stroke="#fff" stroke-width="3" stroke-linecap="round" stroke-linejoin="round"/></svg>Nothing Down - 100% GTU Purchase Financing</li>
      <li><svg viewBox="0 0 28 28"><circle cx="14" cy="14" r="13" fill="var(--check-green)"/><path d="M8 14.5l4 4 8-9" fill="none" stroke="#fff" stroke-width="3" stroke-linecap="round" stroke-linejoin="round"/></svg>One Submission, One Approval and One Closing</li>
      <li><svg viewBox="0 0 28 28"><circle cx="14" cy="14" r="13" fill="var(--check-green)"/><path d="M8 14.5l4 4 8-9" fill="none" stroke="#fff" stroke-width="3" stroke-linecap="round" stroke-linejoin="round"/></svg><span>No Income Limits, No DTI Restrictions,<br>No Property Restrictions</span></li>
    </ul>
  </section>

  <svg class="footer-band" viewBox="0 0 1200 121" preserveAspectRatio="none">
    <path d="M0 0 H500 C520 0 528 6 536 20 L566 88 C574 99 582 103 600 103 H1200 V121 H0 Z" fill="var(--deep-blue)"/>
  </svg>
  <div class="footer-strip"></div>
  <div class="housing-badge"></div>
  <div class="footer-divider"></div>
  <div class="license">RLCB #738160</div>

  <section class="call-to-action">
    <div class="call-number">CALL (800) 471-9026</div>
    <div class="call-sub">FOR MORE INFORMATION</div>
    <div class="call-web">www.2ndlanehomes.com</div>
  </section>
</main>
</body>
</html>
```